HOME IMPROVEMENT Business Card

I want a very unique business card. nothing typical and boring. Im open to you ideas. Ive seen cards with gold and silver or color foil and spot UV coatings. Im looking for something that looks cool and grabs attention. I like rounded corners but am open to all suggestions. We are a home improvement company and I will have a presentation folder printed and a catalog printed also and want to keep that same theme. I love the colors in our logo but I am open at looking at a 3rd color that would work with my logo. I hope that helps.
Card should include
Address
Phone
Fax
Email
Website
Target Market(s)
Home owners, people looking to remodel their home
Industry/Entity Type
Home Improvement
Contact Information for Business Card
2873 Maple Crest Avenue Unit 410
Oak Hollow, IL 60284
Phone
Direct Line
Email
Website
Font styles to use
Other font styles liked:
- IM OPEN MINDED
Requirements
Must have
- High end quality look nothing boring I like rounded corners but am open minded
Nice to have
- WOW. I want something nice and impressive.
Should not have
- ??? Not sure

```html
<!DOCTYPE html>
<html lang="en">
<head>
<meta charset="utf-8">
<title>Keystone Remodeling Group – Business Card</title>
<link href="https://fonts.googleapis.com/css2?family=Libre+Baskerville:wght@400;700&display=swap" rel="stylesheet">
<style>
  :root {
    --backdrop: #141414;
    --card: #1c1c1d;
    --card-edge: #262627;
    --gold: #d9b45a;
    --gold-soft: #c9a24a;
    --silver: #a9a9a9;
  }
  * { box-sizing: border-box; margin: 0; padding: 0; }
  html, body {
    width: 1200px; height: 786px; overflow: hidden;
    background: var(--backdrop);
    font-family: "Libre Baskerville", Georgia, serif;
  }
  .stage {
    width: 1200px; height: 786px;
    display: flex; align-items: center; justify-content: center; gap: 60px;
  }
  .card {
    position: relative;
    width: 525px; height: 300px;
    background: var(--card);
    border: 1px solid var(--card-edge);
    border-radius: 14px;
    overflow: hidden;
  }
  /* Contact side */
  .person { position: absolute; left: 40px; top: 92px; }
  .person-name {
    color: var(--gold); font-size: 19px; letter-spacing: 1.5px; font-weight: 400;
  }
  .person-title {
    color: var(--gold-soft); font-size: 11px; letter-spacing: 1.5px; margin-top: 6px;
  }
  .address {
    position: absolute; left: 300px; top: 92px;
    color: var(--silver); font-size: 10.5px; line-height: 1.7;
    font-style: normal;
  }
  .contacts {
    position: absolute; left: 40px; bottom: 36px;
    list-style: none; color: var(--silver); font-size: 10.5px;
  }
  .contacts li { display: flex; align-items: center; gap: 10px; line-height: 1.85; }
  .contacts svg { width: 10px; height: 10px; fill: var(--gold); flex: none; }
  .contacts .web-name { color: var(--gold); }
  /* Brand side */
  .brand {
    position: absolute; inset: 0;
    display: flex; align-items: center; justify-content: center; gap: 14px;
  }
  .brand-mark { width: 18px; height: 18px; background: var(--gold); flex: none; }
  .brand-name {
    color: var(--gold); font-size: 26px; font-weight: 700; letter-spacing: 1px;
    white-space: nowrap;
  }
</style>
</head>
<body>
<main class="stage">
  <section class="card card-contact">
    <div class="person">
      <h1 class="person-name">DANIEL BROOKS</h1>
      <p class="person-title">CEO/FOUNDER</p>
    </div>
    <address class="address">
      2873 Maple Crest Avenue Unit 410<br>
      Oak Hollow, IL 60284
    </address>
    <ul class="contacts">
      <li>
        <svg viewBox="0 0 10 10" aria-hidden="true"><path d="M2 0.5 L3.6 2.8 L2.8 3.8 Q4 6 6.2 7.2 L7.2 6.4 L9.5 8 L8.4 9.6 Q3.5 9.2 0.4 1.6 Z"/></svg>
        000 000 0000
      </li>
      <li>
        <svg viewBox="0 0 10 10" aria-hidden="true"><path d="M2.5 0.5 H7.5 V3 H2.5 Z M0.5 3.5 H9.5 V7.5 H8 V6 H2 V7.5 H0.5 Z M2.5 6.5 H7.5 V9.5 H2.5 Z"/></svg>
        000 000 0000
      </li>
      <li>
        <svg viewBox="0 0 10 10" aria-hidden="true"><path d="M0.5 2 H9.5 V8 H0.5 Z M1 2.4 L5 5.6 L9 2.4 V3.4 L5 6.6 L1 3.4 Z" fill-rule="evenodd"/></svg>
        hello@keystoneremodel.com
      </li>
      <li>
        <svg viewBox="0 0 10 10" aria-hidden="true"><path d="M5 0.5 A4.5 4.5 0 1 0 5 9.5 A4.5 4.5 0 1 0 5 0.5 Z M5 1.5 A3.5 3.5 0 1 1 5 8.5 A3.5 3.5 0 1 1 5 1.5 Z M1.2 4.5 H8.8 V5.5 H1.2 Z M4.5 1 H5.5 V9 H4.5 Z"/></svg>
        <span>www.<span class="web-name">keystoneremodel</span>.com</span>
      </li>
    </ul>
  </section>

  <section class="card card-brand">
    <div class="brand">
      <span class="brand-mark" aria-hidden="true"></span>
      <p class="brand-name">Keystone Remodeling Group</p>
    </div>
  </section>
</main>
</body>
</html>
```